Business card for Autism Consultancy

I need a double-sided business card for Brightpath Learning Consultancy
Please try to use the colours and graphics in line with our website www.brightpathlearn.nz
Front side
Logo and the name of the company – Brightpath Learning Consultancy
We use Child-Centred, Modern and Innovative approaches
Teaching autistic children to bond, laugh and play
www.brightpathlearn.nz
info@brightpathlearn.nz
phone +64 09 37 615 48
Back side
Photo
Mirela Dunstan
Founder
Postgraduate Autism (Children) Specialist (with Merit)
Qualified by the Faculty of Learning Support and Access Studies (FLSA), Harwell Vale University
mirela@brightpathlearn.nz
phone +64 937 615 48
mobile: +64 20 6283 9150
Please do not convert the text fields to outlines, i.e. I need to be able to edit any text after.
The final design should be either in Adobe Illustrator or Adobe Photoshop format.
The Specs for the business card are:
Full Bleed Size
94 x 58 mm
1110 x 685 pixels
Document Trim Size
91 x 55 mm
1075 x 650 pixels

```html
<!DOCTYPE html>
<html lang="en">
<head>
<meta charset="utf-8">
<title>Brightpath Learning Consultancy – Business Card</title>
<link href="https://fonts.googleapis.com/css2?family=Sansita:wght@700;800&family=Rubik:wght@300;400&display=swap" rel="stylesheet">
<style>
  :root {
    --teal: #56c4bf;
    --navy: #1b2a5c;
    --yellow: #fdd42f;
    --grey-text: #7a7a7a;
    --body-text: #333;
    --white: #ffffff;
    --backdrop: #232323;
  }
  * { margin: 0; padding: 0; box-sizing: border-box; }
  html, body { width: 1200px; height: 741px; overflow: hidden; }
  body { background: var(--backdrop); position: relative; font-family: "Rubik", sans-serif; }

  .card { position: absolute; background: var(--white); border-radius: 18px; overflow: hidden; }

  /* Back side: founder card */
  .founder-card { left: 150px; top: 73px; width: 328px; height: 536px; }
  .founder-card .header-band { position: absolute; left: 0; top: 0; width: 328px; height: 200px; }
  .founder-name {
    position: absolute; top: 30px; width: 100%; text-align: center;
    font-family: "Sansita", sans-serif; font-weight: 800; font-size: 29px;
    color: var(--white); letter-spacing: 1px;
  }
  .portrait-ring {
    position: absolute; left: 66px; top: 82px; width: 192px; height: 192px;
    border-radius: 50%; background: var(--teal); padding: 4px;
  }
  .portrait-ring .inner { width: 100%; height: 100%; border-radius: 50%; background: var(--white); padding: 6px; }
  .portrait {
    width: 100%; height: 100%; border-radius: 50%;
    background: radial-gradient(circle at 50% 40%, #d9a88f 0%, #b07a60 40%, #5a4136 75%, #e9e3de 100%);
  }
  .founder-role {
    position: absolute; top: 280px; width: 100%; text-align: center;
    font-family: "Sansita", sans-serif; font-weight: 800; font-size: 19px; color: var(--navy);
  }
  .credentials {
    position: absolute; top: 313px; width: 100%; text-align: center;
    font-size: 12.5px; font-weight: 300; line-height: 18px; color: var(--grey-text);
  }
  .credentials p + p { margin-top: 6px; }
  .contact-pill {
    position: absolute; left: 50%; transform: translateX(-50%);
    height: 24px; border-radius: 12px; background: var(--yellow);
    display: flex; align-items: center; justify-content: center; gap: 5px;
    font-size: 14.5px; color: var(--body-text); white-space: nowrap;
  }
  .contact-pill svg { width: 12px; height: 12px; fill: var(--body-text); }
  .pill-phone { top: 420px; width: 185px; }
  .pill-mobile { top: 455px; width: 201px; }
  .pill-email { top: 490px; width: 242px; font-size: 14px; }

  /* Front side: company card */
  .company-card { left: 530px; top: 282px; width: 534px; height: 327px; }
  .company-card .base-band { position: absolute; left: 0; bottom: 0; width: 100%; height: 9px; background: var(--navy); }
  .brand-lockup {
    position: absolute; top: 42px; left: 0; width: 100%;
    display: flex; align-items: center; justify-content: center; gap: 12px;
  }
  .brand-mark { width: 30px; height: 30px; border-radius: 50%; background: var(--yellow); }
  .brand-name {
    font-family: "Sansita", sans-serif; font-weight: 800; font-size: 26px;
    color: var(--navy); letter-spacing: 0.5px;
  }
  .tagline {
    position: absolute; left: 38px; top: 158px; width: 462px; height: 47px;
    border-radius: 24px; background: var(--yellow);
    display: flex; flex-direction: column; align-items: center; justify-content: center;
    font-family: "Sansita", sans-serif; font-weight: 700; font-size: 15px; line-height: 19px;
    color: var(--navy); letter-spacing: 0.4px;
  }
  .contact-row {
    position: absolute; top: 242px; left: 0; width: 100%;
    display: flex; justify-content: center; gap: 22px;
    font-size: 15.5px; color: var(--grey-text);
  }
  .contact-row span { display: flex; align-items: center; gap: 10px; }
  .icon-dot {
    width: 20px; height: 20px; border-radius: 50%; background: var(--yellow);
    display: flex; align-items: center; justify-content: center;
  }
  .icon-dot svg { width: 10px; height: 10px; fill: var(--navy); }
  .website {
    position: absolute; top: 278px; width: 100%; text-align: center;
    font-size: 15.5px; color: var(--grey-text); letter-spacing: 0.3px;
  }
  .website strong { font-weight: 400; color: var(--navy); }
</style>
</head>
<body>

<section class="card founder-card">
  <svg class="header-band" viewBox="0 0 328 200" aria-hidden="true">
    <path d="M0 0H328V186Q300 180 270 188Q230 200 164 200Q98 200 58 188Q28 180 0 190Z" fill="var(--teal)"/>
  </svg>
  <h1 class="founder-name">Mirela Dunstan</h1>
  <div class="portrait-ring"><div class="inner">
    <div class="portrait" role="img" aria-label="Portrait photo of the founder"></div>
  </div></div>
  <h2 class="founder-role">Founder</h2>
  <div class="credentials">
    <p>Postgraduate Autism (Children)<br>Specialist (with Merit)</p>
    <p>Qualified by the Faculty of<br>Learning Support and Access Studies (FLSA),<br>Harwell Vale University</p>
  </div>
  <div class="contact-pill pill-phone">
    <svg viewBox="0 0 12 12"><path d="M1 4Q1 2 3 2H9Q11 2 11 4V5H8V4H4V5H1ZM2 6H10L11 10H1Z"/></svg>
    +64 937 615 48
  </div>
  <div class="contact-pill pill-mobile">
    <svg viewBox="0 0 12 12"><path d="M3 0H9V12H3ZM4 1.5V9.5H8V1.5Z"/></svg>
    +64 20 6283 9150
  </div>
  <div class="contact-pill pill-email">
    <svg viewBox="0 0 12 12"><path d="M0 2H12V10H0ZM1 3V3.3L6 6.5L11 3.3V3Z"/></svg>
    mirela@brightpathlearn.nz
  </div>
</section>

<section class="card company-card">
  <div class="brand-lockup">
    <span class="brand-mark"></span>
    <span class="brand-name">Brightpath Learning Consultancy</span>
  </div>
  <div class="tagline">
    <span>We use Child-Centred, Modern and Innovative approaches</span>
    <span>Teaching autistic children to bond, laugh and play</span>
  </div>
  <div class="contact-row">
    <span><i class="icon-dot"><svg viewBox="0 0 12 12"><path d="M1 4Q1 2 3 2H9Q11 2 11 4V5H8V4H4V5H1ZM2 6H10L11 10H1Z"/></svg></i>+64 09 37 615 48</span>
    <span><i class="icon-dot"><svg viewBox="0 0 12 12"><path d="M0 2H12V10H0ZM1 3V3.3L6 6.5L11 3.3V3Z"/></svg></i>info@brightpathlearn.nz</span>
  </div>
  <p class="website">www.<strong>brightpathlearn</strong>.nz</p>
  <div class="base-band"></div>
</section>

</body>
</html>
```